Halvorn spray foam and Environmental

I have business cards but need new ones. The ones I have are very bland. Here is. Y company website http://www.halvornsprayfoam.ca

Also I can send you copies of the current cards
I would also need my current logo on the new design as well.. Also spray foam and Environmental

Industry/Entity Type

Business

Logo Text

Halvorn.

```html
<!DOCTYPE html>
<html lang="en">
<head>
<meta charset="utf-8">
<title>Halvorn Business Card</title>
<link rel="stylesheet" href="https://fonts.googleapis.com/css2?family=Open+Sans:wght@400;600;700;800&family=EB+Garamond:wght@400&display=swap">
<style>
  :root {
    --page: #dcdcde;
    --white: #ffffff;
    --purple: #6a3a86;
    --purple-deep: #3e0f4f;
    --purple-mid: #6b2d84;
    --purple-text: #5a2a78;
    --green: #58bb43;
    --green-line: #8fd17f;
    --ink: #444444;
    --grey: #777777;
  }
  * { box-sizing: border-box; margin: 0; padding: 0; }
  html, body { width: 1200px; height: 1200px; overflow: hidden; }
  body {
    background: var(--page);
    font-family: "Open Sans", sans-serif;
    position: relative;
  }
  .card {
    position: absolute;
    left: 250px;
    width: 700px;
    height: 400px;
    overflow: hidden;
    box-shadow: 0 6px 18px rgba(0,0,0,0.12);
  }
  .card--front { top: 140px; background: var(--white); }
  .card--back {
    top: 660px;
    background: radial-gradient(ellipse at 55% 45%, #6d2f88 0%, #541f6e 45%, var(--purple-deep) 100%);
  }

  /* front */
  .brand {
    position: absolute;
    left: 70px; top: 44px;
    width: 320px;
    text-align: center;
  }
  .brand__row { display: flex; align-items: center; justify-content: center; gap: 12px; }
  .brand__mark { width: 34px; height: 34px; background: var(--purple-text); }
  .brand__name {
    font-weight: 800; font-size: 30px; letter-spacing: 0.5px;
    color: var(--purple-text); text-transform: uppercase;
  }
  .brand__sub {
    font-size: 11px; font-weight: 600; letter-spacing: 1px;
    color: var(--green); margin-top: 2px; padding-left: 46px;
  }
  .brand__tagline {
    font-family: "EB Garamond", serif; font-size: 21px;
    color: var(--green); margin-top: 2px;
    display: flex; align-items: center; gap: 10px; justify-content: center;
  }
  .brand__tagline::before, .brand__tagline::after {
    content: ""; width: 30px; height: 1px; background: #bbbbbb;
  }
  .person { position: absolute; left: 70px; top: 170px; width: 600px; }
  .person__name { font-weight: 700; font-size: 26px; color: var(--purple-text); line-height: 1; }
  .person__role {
    font-size: 14px; color: var(--grey); margin-top: 4px;
    display: flex; align-items: center; gap: 10px;
  }
  .person__role::after { content: ""; flex: 1; height: 1px; background: var(--green-line); }
  .contacts { position: absolute; left: 70px; top: 236px; list-style: none; }
  .contacts li {
    display: flex; align-items: center; gap: 10px;
    font-size: 15px; color: var(--ink); height: 26px;
  }
  .icon {
    width: 18px; height: 18px; border-radius: 4px; background: var(--green);
    display: inline-flex; align-items: center; justify-content: center;
  }
  .address {
    position: absolute; right: 40px; top: 258px;
    display: flex; align-items: center; gap: 10px;
    font-size: 14px; color: var(--ink); text-align: right; line-height: 1.35;
  }
  .band { position: absolute; left: 0; bottom: 0; width: 700px; height: 62px; }

  /* back */
  .back-rule {
    position: absolute; left: 60px; right: 60px; top: 200px;
    height: 1px; background: rgba(40,0,60,0.35);
  }
  .back-brand {
    position: absolute; left: 0; right: 0; top: 130px; text-align: center;
  }
  .back-brand__row { display: flex; align-items: center; justify-content: center; gap: 14px; }
  .back-brand__mark { width: 46px; height: 46px; background: #3a0c4d; }
  .back-brand__name {
    font-weight: 800; font-size: 40px; color: #3a0c4d; text-transform: uppercase;
  }
  .back-brand__sub {
    font-size: 14px; font-weight: 600; letter-spacing: 1px; color: #3a0c4d;
    padding-left: 60px; margin-top: 0;
  }
  .back-brand__tagline {
    font-family: "EB Garamond", serif; font-size: 30px; color: #7e4a97; margin-top: 4px;
  }
</style>
</head>
<body>

<section class="card card--front" aria-label="Business card front">
  <div class="brand">
    <div class="brand__row">
      <span class="brand__mark"></span>
      <span class="brand__name">Halvorn</span>
    </div>
    <div class="brand__sub">ENVIRONMENTAL</div>
    <div class="brand__tagline">Residential &amp; Commercial</div>
  </div>

  <div class="person">
    <div class="person__name">JOHN DOE</div>
    <div class="person__role">Director</div>
  </div>

  <ul class="contacts">
    <li>
      <span class="icon"><svg width="12" height="12" viewBox="0 0 24 24"><path fill="#fff" d="M6.6 10.8a15 15 0 0 0 6.6 6.6l2.2-2.2a1 1 0 0 1 1-.25 11.4 11.4 0 0 0 3.6.57 1 1 0 0 1 1 1V20a1 1 0 0 1-1 1A17 17 0 0 1 3 4a1 1 0 0 1 1-1h3.5a1 1 0 0 1 1 1c0 1.25.2 2.45.57 3.57a1 1 0 0 1-.25 1z"/></svg></span>
      (604) 555-0187
    </li>
    <li>
      <span class="icon"><svg width="12" height="12" viewBox="0 0 24 24"><path fill="#fff" d="M2 5h20v14H2zm2 2v.5l8 5 8-5V7l-8 5z"/></svg></span>
      enviro@halvornmail.com
    </li>
    <li>
      <span class="icon"><svg width="12" height="12" viewBox="0 0 24 24"><circle cx="12" cy="12" r="9" fill="none" stroke="#fff" stroke-width="2"/><path d="M3 12h18M12 3c3 3 3 15 0 18M12 3c-3 3-3 15 0 18" fill="none" stroke="#fff" stroke-width="1.6"/></svg></span>
      www.halvornenvironmental.ca
    </li>
  </ul>

  <div class="address">
    <span>4820 Larchmont Way Burnaby<br>British Columbia v5e 2k4, CA</span>
    <span class="icon"><svg width="12" height="12" viewBox="0 0 24 24"><path fill="#fff" d="M12 2a7 7 0 0 0-7 7c0 5 7 13 7 13s7-8 7-13a7 7 0 0 0-7-7zm0 9.5A2.5 2.5 0 1 1 12 6.5a2.5 2.5 0 0 1 0 5z"/></svg></span>
  </div>

  <svg class="band" viewBox="0 0 700 62" preserveAspectRatio="none" aria-hidden="true">
    <polygon points="0,0 440,0 470,62 0,62" fill="var(--purple)"/>
    <polygon points="440,0 700,0 700,62 470,62" fill="var(--green)"/>
  </svg>
</section>

<section class="card card--back" aria-label="Business card back">
  <div class="back-rule"></div>
  <div class="back-brand">
    <div class="back-brand__row">
      <span class="back-brand__mark"></span>
      <span class="back-brand__name">Halvorn</span>
    </div>
    <div class="back-brand__sub">SPRAY FOAM LTD.</div>
    <div class="back-brand__tagline">Residential &amp; Commercial</div>
  </div>
</section>

</body>
</html>
```